Caldrow Supplies Business Card

Professional business card that stand out to our potential customers. Front and back with clean modern design

Industry/Entity Type

Oil and gas

Contact Information for Business Card

Name, address, website , office phone and cell number

Requirements
Must have
• Editable files for each employee

```html
<!DOCTYPE html>
<html lang="en">
<head>
<meta charset="utf-8">
<title>Caldrow Supplies Business Card</title>
<link rel="stylesheet" href="https://fonts.googleapis.com/css2?family=Montserrat:wght@400;500;700;800&display=swap">
<style>
:root{
  --bg:#222222;
  --red:#ff0000;
  --white:#ffffff;
  --blue:#03b2d4;
}
*{margin:0;padding:0;box-sizing:border-box}
html,body{width:1200px;height:711px;overflow:hidden;background:var(--bg)}
body{font-family:"Montserrat",Arial,sans-serif;position:relative}
.card{
  position:absolute;top:86px;width:310px;height:540px;border-radius:22px;
  background:var(--red);overflow:hidden;box-shadow:0 10px 24px rgba(0,0,0,.55);
}
.card-back{left:255px}
.card-front{left:635px}

/* back */
.back-brand{
  position:absolute;left:0;right:0;top:230px;display:flex;flex-direction:column;
  align-items:center;gap:18px;
}
.brand-square{width:74px;height:74px;background:var(--blue);border:5px solid var(--white)}
.back-brand .brand-name{color:var(--white);font-weight:800;font-size:22px;letter-spacing:2px}

/* front */
.front-top{
  position:absolute;left:0;top:0;width:100%;height:260px;background:var(--white);
  clip-path:polygon(0 0,100% 0,100% 56%,0 100%);
}
.front-brand{
  position:absolute;left:24px;right:24px;top:30px;text-align:center;
  color:var(--red);font-weight:800;font-size:17px;letter-spacing:1.5px;white-space:nowrap;
}
.front-mark{
  position:absolute;left:50%;top:84px;width:112px;height:112px;margin-left:-56px;
  background:var(--blue);border:6px solid var(--red);
}
.person{position:absolute;left:0;right:0;top:292px;text-align:center;color:var(--white)}
.person-name{font-weight:800;font-size:23px;letter-spacing:1px}
.person-title{display:flex;align-items:center;justify-content:center;gap:10px;font-size:13px;margin-top:2px}
.person-title::before,.person-title::after{content:"";width:64px;height:1.5px;background:var(--white)}
.icons{display:flex;justify-content:center;gap:14px;margin:20px 0 14px}
.icon{width:28px;height:28px;background:var(--blue);display:flex;align-items:center;justify-content:center}
.icon svg{width:18px;height:18px}
.contact{list-style:none;font-size:13px;line-height:19px;font-weight:500}
.divider{width:220px;height:1.5px;background:var(--white);margin:12px auto}
.address{font-size:13px;line-height:19px;font-weight:500}
</style>
</head>
<body>
  <section class="card card-back">
    <div class="back-brand">
      <div class="brand-square"></div>
      <div class="brand-name">CALDROW SUPPLIES</div>
    </div>
  </section>

  <section class="card card-front">
    <div class="front-top"></div>
    <div class="front-brand">CALDROW SUPPLIES</div>
    <div class="front-mark"></div>
    <div class="person">
      <div class="person-name">DALEN OSTROW</div>
      <div class="person-title">President</div>
      <div class="icons">
        <span class="icon"><svg viewBox="0 0 24 24" fill="#fff"><path d="M6.6 10.8a15 15 0 006.6 6.6l2.2-2.2c.3-.3.7-.4 1-.2 1.1.4 2.3.6 3.6.6.6 0 1 .4 1 1V20c0 .6-.4 1-1 1A17 17 0 013 4c0-.6.4-1 1-1h3.5c.6 0 1 .4 1 1 0 1.3.2 2.5.6 3.6.1.3 0 .7-.2 1z"/></svg></span>
        <span class="icon"><svg viewBox="0 0 24 24" fill="none" stroke="#fff" stroke-width="2"><rect x="7" y="2" width="10" height="20" rx="2"/><line x1="11" y1="18" x2="13" y2="18"/></svg></span>
        <span class="icon"><svg viewBox="0 0 24 24" fill="none" stroke="#fff" stroke-width="2"><rect x="3" y="5" width="18" height="14"/><polyline points="3,5 12,13 21,5"/></svg></span>
        <span class="icon"><svg viewBox="0 0 24 24" fill="none" stroke="#fff" stroke-width="2"><circle cx="12" cy="12" r="9"/><ellipse cx="12" cy="12" rx="4" ry="9"/><line x1="3" y1="12" x2="21" y2="12"/></svg></span>
      </div>
      <ul class="contact">
        <li>555-201-4417</li>
        <li>555-201-0093</li>
        <li>info@caldrowsupplies.com</li>
        <li>www.caldrowsupplies.com</li>
      </ul>
      <div class="divider"></div>
      <p class="address">482 Orren Ave, Ste<br>100, Bramley, TX 75290</p>
    </div>
  </section>
</body>
</html>
```